Home care support

Design a a great and dynamic website for a healthcare business. Our business will be involved in providing care at home for people with disability and the elderly. Below is a link that I found for a company offering similar services in the US. I am looking for something like this .
I have my files - the latest project in here in through through Pixelmarket
Sample site : https://cedarbrookassistedliving.com/
Target Market(s)
people with disability and elderly seniors who need home care support
Industry/Entity Type
Health
Coding
Coded - Design and coding required
Number of Pages Required
5+ page
Requirements
Must have
- inspirational pictures and designed with the themed logo (files attached)
Nice to have
- This is my sample and should look like this : https://cedarbrookassistedliving.com/

```html
<!DOCTYPE html>
<html lang="en">
<head>
<meta charset="utf-8">
<title>Larkhaven Home Care</title>
<link href="https://fonts.googleapis.com/css2?family=Cinzel:wght@400;600&family=Roboto:wght@400;500;700&display=swap" rel="stylesheet">
<style>
:root{
  --blue:#1a7fd0;
  --blue-dark:#0f6cb8;
  --green:#5a8f31;
  --ink:#222;
  --muted:#555;
  --black:#000;
  --white:#fff;
}
*{box-sizing:border-box;margin:0;padding:0}
html,body{width:1200px;height:3476px;overflow:hidden}
body{position:relative;font-family:Roboto,Arial,sans-serif;color:var(--ink);background:var(--white)}
.abs{position:absolute}
.serif{font-family:Cinzel,Georgia,serif}
.btn{position:absolute;display:flex;align-items:center;justify-content:center;gap:9px;border-radius:26px;color:var(--white);font-weight:700;font-size:14px;text-transform:uppercase}
.btn .dot{width:13px;height:13px;border-radius:50%;background:var(--white);position:relative}
.btn .dot::after{content:"";position:absolute;left:4px;top:3.5px;border-left:6px solid currentColor;border-top:3px solid transparent;border-bottom:3px solid transparent}
.btn.blue{background:var(--blue)}.btn.blue .dot::after{border-left-color:var(--blue)}
.btn.green{background:var(--green)}.btn.green .dot::after{border-left-color:var(--green)}

/* top bar */
.topbar{left:0;top:0;width:1200px;height:48px;background:var(--blue);color:var(--white);font-size:14px}
.topbar .mail{left:113px;top:15px}
.topbar .social{left:536px;top:12px;display:flex;gap:8px}
.topbar .social span{width:25px;height:25px;border:1.5px solid var(--white);border-radius:50%}
.topbar .phone{right:110px;top:13px;font-weight:700;font-size:16px}

/* nav */
.nav{left:0;top:48px;width:1200px;height:77px;background:var(--white)}
.brand{left:98px;top:42px;width:140px;height:125px;border-radius:0 0 70px 70px;background:var(--white);z-index:3;display:flex;align-items:center;justify-content:center;text-align:center;font-family:Cinzel,Georgia,serif;font-weight:600;font-size:19px;line-height:1.1;color:var(--blue-dark)}
.menu{left:294px;top:80px;display:flex;gap:30px;font-size:14px;font-weight:500;z-index:4}
.menu .on{color:var(--blue)}
.menu-cta{left:866px;top:63px;width:222px;height:47px;z-index:4}

/* hero */
.hero{left:0;top:125px;width:1200px;height:695px;background:linear-gradient(100deg,#c9c2b6 0%,#b8a99c 25%,#7f8a72 55%,#5f7552 80%,#4f6348 100%)}
.hero-copy{left:630px;top:300px;color:var(--white);z-index:2}
.hero-copy h1{font-family:Cinzel,Georgia,serif;font-weight:600;font-size:50px;line-height:56px;letter-spacing:1px}
.hero-copy p{margin-top:24px;font-size:17px;line-height:25px;font-weight:500;width:460px}
.hero-cta{left:630px;top:517px;width:223px;height:47px;z-index:2}
.arrow-box{width:44px;height:26px;background:var(--white);top:426px;z-index:2}

/* section heads */
.kicker{width:1200px;text-align:center;font-size:13px;font-weight:700;color:var(--ink)}
.sec-title{width:1200px;text-align:center;font-family:Cinzel,Georgia,serif;font-size:29px;letter-spacing:1px;color:var(--blue)}
.rule{height:2px;background:var(--blue)}

/* services */
.service{width:230px;text-align:center}
.service .disc{width:156px;height:156px;border-radius:50%;margin:0 auto;display:flex;align-items:center;justify-content:center}
.service h3{margin-top:30px;font-family:Cinzel,Georgia,serif;font-weight:600;font-size:16px;letter-spacing:.5px;color:var(--ink)}
.service .bar{width:36px;height:2px;margin:14px auto 0}
.service p{margin-top:16px;font-size:14px;line-height:20px;color:var(--muted);text-align:justify;text-align-last:center}
.service .more{margin-top:14px;display:inline-flex;align-items:center;gap:8px;font-size:12.5px;font-weight:700;text-decoration:underline}
.service .more i{width:11px;height:11px;border-radius:50%;background:currentColor;display:inline-block}

/* about */
.about-panel{left:0;top:1435px;width:612px;height:528px;background:var(--blue);border-top-left-radius:150px 330px}
.about-copy{left:111px;top:1510px;width:446px;color:var(--white)}
.about-copy .k{font-size:13px;font-weight:700}
.about-copy .r{width:140px;height:2px;background:var(--white);margin-top:6px}
.about-copy h2{font-family:Cinzel,Georgia,serif;font-weight:400;font-size:28px;letter-spacing:1px;margin-top:4px}
.about-copy p{margin-top:20px;font-size:14.3px;line-height:24.8px;text-align:justify}
.about-cta{left:112px;top:1836px;width:163px;height:46px}
.about-photo{left:612px;top:1435px;width:588px;height:528px;background:linear-gradient(120deg,#e8e3dc 0%,#d9cfc3 40%,#cfb79a 60%,#b9c4c6 100%);border-bottom-right-radius:260px 290px}

/* why */
.why-bg{left:0;top:1963px;width:1200px;height:577px;background:var(--white)}
.why-item{width:260px}
.why-item h4{font-family:Cinzel,Georgia,serif;font-weight:400;font-size:17px;letter-spacing:.5px}
.why-item p{margin-top:6px;font-size:13.5px;line-height:18px;color:var(--muted)}
.why-item.l{text-align:right}
.why-item.g h4{color:var(--green)}
.why-item.b h4{color:var(--blue)}
.ico{width:62px;height:62px;border-radius:50%;display:flex;align-items:center;justify-content:center;box-shadow:0 6px 10px rgba(0,0,0,.2)}
.ico.g{background:var(--green)}.ico.b{background:var(--blue)}
.hub{left:450px;top:2142px;width:300px;height:300px;border-radius:50%;background:var(--blue);box-shadow:0 10px 22px rgba(0,0,0,.25);display:flex;align-items:center;justify-content:center}
.hub-inner{width:232px;height:232px;border-radius:50%;background:var(--white);border:4px solid var(--blue-dark);display:flex;align-items:center;justify-content:center;text-align:center;font-family:Cinzel,Georgia,serif;font-weight:600;font-size:22px;line-height:1.2;color:var(--blue-dark)}

/* contact */
.contact{left:0;top:2540px;width:1200px;height:470px;background:linear-gradient(180deg,#5f9535 0%,#5a8f31 60%,#4e8229 100%)}
.contact .kicker,.contact .sec-title{color:var(--white)}
.field{position:absolute;background:var(--white);border:1px solid #d6d6d6;font-size:14px;color:#555;padding:0 18px;display:flex;align-items:center}
.field.msg{align-items:flex-start;padding-top:15px}

/* footer */
.footer{left:0;top:3010px;width:1200px;height:466px;background:var(--black)}
.fcol{color:var(--white)}
.fcol h5{font-size:14px;font-weight:700;text-transform:uppercase}
.fcol .u{width:58px;height:2px;background:var(--white);margin-top:6px}
.fcol p{font-size:13.5px;line-height:24px}
.ring{width:40px;height:40px;border:1px solid #777;border-radius:50%;display:flex;align-items:center;justify-content:center}
.fsoc{display:flex;gap:6px}
.fsoc span{width:40px;height:40px;border:1px solid #888;border-radius:50%}
.links li{list-style:none;font-size:14px;line-height:32px}
.links li::before{content:"»";margin-right:12px}
.subscribe{width:220px;height:46px;background:var(--white);border-radius:3px;display:flex}
.subscribe span{flex:1;padding-left:16px;font-size:14px;color:#555;display:flex;align-items:center}
.subscribe b{width:44px;background:var(--blue);border:2px solid var(--white);display:flex;align-items:center;justify-content:center}
.copy{left:0;top:3430px;width:1200px;text-align:center;color:var(--white);font-size:14px}
.fline{left:114px;top:3405px;width:972px;height:1px;background:#444}
</style>
</head>
<body>

<!-- top bar -->
<div class="abs topbar">
  <div class="abs mail">
    <svg width="16" height="12" viewBox="0 0 16 12" style="vertical-align:-1px;margin-right:10px"><rect width="16" height="12" rx="1" fill="#fff"/><path d="M1 1l7 6 7-6" stroke="#1a7fd0" stroke-width="1.4" fill="none"/></svg>hello@larkhaven.example
  </div>
  <div class="abs social"><span></span><span></span><span></span><span></span></div>
  <div class="abs phone">
    <svg width="14" height="14" viewBox="0 0 24 24" style="vertical-align:-2px;margin-right:10px"><path fill="#fff" d="M6.6 10.8a15 15 0 006.6 6.6l2.2-2.2c.3-.3.7-.4 1-.2 1.1.4 2.3.6 3.6.6.6 0 1 .4 1 1V20c0 .6-.4 1-1 1A17 17 0 013 4c0-.6.4-1 1-1h3.5c.6 0 1 .4 1 1 0 1.3.2 2.5.6 3.6.1.3 0 .7-.2 1z"/></svg>+1 555 010 2200
  </div>
</div>

<!-- nav -->
<div class="abs nav"></div>
<div class="abs brand">Larkhaven<br>Home Care</div>
<nav class="abs menu">
  <span class="on">Home</span><span>About</span><span>Services</span><span>FAQ</span><span>Resources</span><span>Employment</span><span>Contact</span>
</nav>
<div class="btn green menu-cta">Make an appointment <span class="dot"></span></div>

<!-- hero -->
<div class="abs hero" role="img" aria-label="Photo of a young carer smiling with an elderly woman outdoors"></div>
<svg class="abs" style="left:0;top:125px;z-index:1" width="1200" height="695" viewBox="0 0 1200 695">
  <path d="M0,492 Q600,726 1200,492" stroke="#fff" stroke-width="4" fill="none"/>
  <path d="M0,503 Q600,737 1200,503 L1200,523 Q600,827 0,523 Z" fill="#1a7fd0"/>
  <path d="M0,523 Q600,827 1200,523 L1200,695 L0,695 Z" fill="#fff"/>
</svg>
<div class="abs arrow-box" style="left:25px"><svg width="44" height="26" viewBox="0 0 44 26"><path d="M12 13h20M12 13l5-5M12 13l5 5" stroke="#000" stroke-width="2.5" fill="none"/></svg></div>
<div class="abs arrow-box" style="left:1131px"><svg width="44" height="26" viewBox="0 0 44 26"><path d="M12 13h20M32 13l-5-5M32 13l-5 5" stroke="#000" stroke-width="2.5" fill="none"/></svg></div>
<div class="abs hero-copy">
  <h1>THE BEST CARE IS<br>HOME CARE</h1>
  <p>Lorem ipsum dolor sit amet, consectetur adipiscing elised do eiusmod tempor incididunt ut labore</p>
</div>
<div class="btn blue hero-cta">Make an appointment <span class="dot"></span></div>

<!-- services -->
<div class="abs kicker" style="left:0;top:852px">WHAT WE DO</div>
<div class="abs rule" style="left:498px;top:874px;width:204px"></div>
<div class="abs sec-title" style="left:0;top:878px">OUR SERVICES</div>

<div class="abs service" style="left:101px;top:943px">
  <div class="disc" style="background:var(--blue)"><svg width="80" height="80" viewBox="0 0 80 80"><path d="M40 38c-10-8-16-12-16-19a8 8 0 0116-2 8 8 0 0116 2c0 7-6 11-16 19z" fill="#fff"/><path d="M10 54l12-8h14c3 0 3 5 0 5h-8h10l14-8c3-2 6 2 3 4L38 62H10z" fill="#fff"/></svg></div>
  <h3>COMPANION CARE</h3><div class="bar" style="background:var(--blue)"></div>
  <p>Lorem ipsum dolor sit consectetur adipiscing elit, sed do eiusmod tempor incididunt</p>
  <span class="more" style="color:var(--blue)">LEARN MORE <i></i></span>
</div>
<div class="abs service" style="left:357px;top:943px">
  <div class="disc" style="background:var(--green)"><svg width="80" height="80" viewBox="0 0 80 80"><rect x="34" y="12" width="10" height="14" fill="#fff"/><rect x="24" y="24" width="30" height="12" fill="#fff"/><path d="M12 38h56l-6 14H18z" fill="#fff"/><path d="M12 60q7-5 14 0t14 0 14 0 14 0M12 68q7-5 14 0t14 0 14 0 14 0" stroke="#fff" stroke-width="3" fill="none"/></svg></div>
  <h3>TRANSPORTATION</h3><div class="bar" style="background:var(--green)"></div>
  <p>Lorem ipsum dolor sit consectetur adipiscing elit, sed do eiusmod tempor incididunt</p>
  <span class="more" style="color:var(--green)">LEARN MORE <i></i></span>
</div>
<div class="abs service" style="left:613px;top:943px">
  <div class="disc" style="background:var(--blue)"><svg width="80" height="80" viewBox="0 0 80 80"><path d="M10 20h10l8 30h32l6-22H24" stroke="#fff" stroke-width="5" fill="none"/><path d="M26 28h38l-6 18H30z" fill="#fff"/><circle cx="32" cy="60" r="5" fill="#fff"/><circle cx="54" cy="60" r="5" fill="#fff"/></svg></div>
  <h3>SHOPPING &amp; ERRANDS</h3><div class="bar" style="background:var(--blue)"></div>
  <p>Lorem ipsum dolor sit consectetur adipiscing elit, sed do eiusmod tempor incididunt</p>
  <span class="more" style="color:var(--blue)">LEARN MORE <i></i></span>
</div>
<div class="abs service" style="left:869px;top:943px">
  <div class="disc" style="background:var(--green)"><svg width="80" height="80" viewBox="0 0 80 80"><rect x="38" y="10" width="4" height="12" fill="#fff"/><path d="M40 20c-12 0-18 10-18 24h36c0-14-6-24-18-24z" fill="#fff"/><path d="M34 48a6 6 0 0012 0z" fill="#fff"/><path d="M40 58v10M24 54l-6 8M56 54l6 8" stroke="#fff" stroke-width="4"/></svg></div>
  <h3>LIGHT HOUSEKEEPING</h3><div class="bar" style="background:var(--green)"></div>
  <p>Lorem ipsum dolor sit consectetur adipiscing elit, sed do eiusmod tempor incididunt</p>
  <span class="more" style="color:var(--green)">LEARN MORE <i></i></span>
</div>
<div class="btn blue" style="left:497px;top:1313px;width:206px;height:47px">View all services <span class="dot"></span></div>

<!-- about -->
<div class="abs about-panel"></div>
<div class="abs about-copy">
  <div class="k">WHO WE ARE</div><div class="r"></div>
  <h2>ABOUT US</h2>
  <p>Sed ut perspiciatis unde omnis iste natus error sit voluptatem accusantium doloremque laudantium, totam rem aperiam, eaque ipsa quae ab illo inventore veritatis et quasi architecto beatae vitae dicta sunt explicabo. Nemo enim ipsam voluptatem quia voluptas sit aspernatur aut odit aut fugit, sed quia consequuntur magni dolores eos qui ratione voluptatem sequi nesciunt. Neque porro quisquam est, qui dolorem ipsum quia dolor sit amet, consectetur, adipisci velit, sed quia non numquam eius modi tempora incidunt ut labore et dolore magnam aliquam quaerat voluptatem.</p>
</div>
<div class="btn green about-cta">Learn more <span class="dot"></span></div>
<div class="abs about-photo" role="img" aria-label="Photo of a smiling carer embracing an elderly woman at home"></div>

<!-- why -->
<div class="abs why-bg"></div>
<div class="abs kicker" style="left:0;top:2039px">WHY US</div>
<div class="abs rule" style="left:478px;top:2062px;width:244px"></div>
<div class="abs sec-title" style="left:0;top:2064px">WHY CHOOSE US</div>

<div class="abs why-item l g" style="left:122px;top:2140px"><h4>FLEXIBLE SCHEDULE</h4><p>Nam libero tempore, cum soluta nobis est eligendi optio cumque nihil</p></div>
<div class="abs ico g" style="left:406px;top:2140px"><svg width="30" height="30" viewBox="0 0 30 30"><rect x="3" y="6" width="24" height="20" rx="2" fill="none" stroke="#fff" stroke-width="2.5"/><path d="M3 12h24M9 3v6M21 3v6" stroke="#fff" stroke-width="2.5"/></svg></div>
<div class="abs why-item l b" style="left:80px;top:2252px"><h4>FREE IN HOME ASSESSMENTS</h4><p>Nam libero tempore, cum soluta nobis est eligendi optio cumque nihil</p></div>
<div class="abs ico b" style="left:364px;top:2252px"><svg width="30" height="30" viewBox="0 0 30 30"><rect x="6" y="4" width="18" height="23" rx="2" fill="none" stroke="#fff" stroke-width="2.5"/><path d="M10 12l2 2 4-4M10 20l2 2 4-4" stroke="#fff" stroke-width="2" fill="none"/></svg></div>
<div class="abs why-item l g" style="left:112px;top:2364px"><h4>PEACE OF MIND</h4><p>Nam libero tempore, cum soluta nobis est eligendi optio cumque nihil</p></div>
<div class="abs ico g" style="left:396px;top:2364px"><svg width="30" height="30" viewBox="0 0 30 30"><path d="M5 17l6 6 14-14" stroke="#fff" stroke-width="3" fill="none"/></svg></div>

<div class="abs ico b" style="left:723px;top:2140px"><svg width="30" height="30" viewBox="0 0 30 30"><circle cx="11" cy="8" r="4" fill="#fff"/><circle cx="21" cy="11" r="3" fill="#fff"/><path d="M5 26v-8a6 6 0 0112 0v8zM17 26v-6a4 4 0 018 0v6z" fill="#fff"/></svg></div>
<div class="abs why-item r b" style="left:810px;top:2140px"><h4>CHOICE OF CAREGIVER</h4><p>Nam libero tempore, cum soluta nobis est eligendi optio cumque nihil</p></div>
<div class="abs ico g" style="left:771px;top:2252px"><svg width="30" height="30" viewBox="0 0 30 30"><circle cx="15" cy="9" r="4" fill="#fff"/><circle cx="7" cy="12" r="3" fill="#fff"/><circle cx="23" cy="12" r="3" fill="#fff"/><path d="M9 24a6 6 0 0112 0zM2 24a5 5 0 019-2v2zM28 24a5 5 0 00-9-2v2z" fill="#fff"/></svg></div>
<div class="abs why-item r g" style="left:860px;top:2252px"><h4>FRIENDLY STAFF</h4><p>Nam libero tempore, cum soluta nobis est eligendi optio cumque nihil</p></div>
<div class="abs ico b" style="left:732px;top:2364px"><svg width="28" height="28" viewBox="0 0 24 24"><path fill="#fff" d="M6.6 10.8a15 15 0 006.6 6.6l2.2-2.2c.3-.3.7-.4 1-.2 1.1.4 2.3.6 3.6.6.6 0 1 .4 1 1V20c0 .6-.4 1-1 1A17 17 0 013 4c0-.6.4-1 1-1h3.5c.6 0 1 .4 1 1 0 1.3.2 2.5.6 3.6.1.3 0 .7-.2 1z"/></svg></div>
<div class="abs why-item r b" style="left:820px;top:2364px"><h4>ON CALL 24/7</h4><p>Nam libero tempore, cum soluta nobis est eligendi optio cumque nihil</p></div>

<div class="abs hub"><div class="hub-inner">Larkhaven<br>Home Care</div></div>

<!-- contact -->
<div class="abs contact" role="img" aria-label="Green-toned photo of a carer assisting a client at home"></div>
<div class="abs kicker" style="left:0;top:2606px;color:#fff">WHAT WE DO</div>
<div class="abs rule" style="left:498px;top:2628px;width:204px;background:#fff"></div>
<div class="abs sec-title" style="left:0;top:2632px;color:#fff">OUR SERVICES</div>
<div class="field" style="left:116px;top:2703px;width:236px;height:52px">First Name</div>
<div class="field" style="left:360px;top:2703px;width:236px;height:52px">Email Address</div>
<div class="field" style="left:604px;top:2703px;width:236px;height:52px">Phone No</div>
<div class="field" style="left:848px;top:2703px;width:237px;height:52px">Address</div>
<div class="field msg" style="left:116px;top:2764px;width:969px;height:87px">Message</div>
<div class="btn blue" style="left:520px;top:2886px;width:161px;height:47px">Submit now <span class="dot"></span></div>

<!-- footer -->
<div class="abs footer"></div>
<svg class="abs" style="left:0;top:2940px" width="1200" height="220" viewBox="0 0 1200 220">
  <path d="M0,0 H1200 V192 Q600,-146 0,192 Z" fill="#4e8229"/>
  <path d="M0,192 Q600,-146 1200,192 L1200,202 Q600,-50 0,202 Z" fill="#1a7fd0"/>
  <path d="M0,204 Q600,-48 1200,204" stroke="#fff" stroke-width="3" fill="none"/>
</svg>

<div class="abs fcol" style="left:116px;top:3160px;width:260px">
  <h5>About us</h5><div class="u"></div>
  <p style="margin-top:18px">Sed ut perspiciatis unde omnis iste natus error sit voluptatem accusantidoloremque laudantium, totam rem aperiam.</p>
  <div class="fsoc" style="margin-top:16px"><span></span><span></span><span></span><span></span></div>
</div>
<div class="abs fcol" style="left:419px;top:3160px;width:260px">
  <h5>Contact us</h5><div class="u"></div>
  <div style="display:flex;gap:16px;margin-top:20px;align-items:flex-start"><div class="ring"><svg width="12" height="16" viewBox="0 0 12 16"><path d="M6 0a6 6 0 016 6c0 4-6 10-6 10S0 10 0 6a6 6 0 016-6z" fill="#fff"/><circle cx="6" cy="6" r="2" fill="#000"/></svg></div><p style="padding-top:5px;line-height:22px">6 , Lorem Ipsum Dolor sit<br>Fantome</p></div>
  <div style="display:flex;gap:16px;margin-top:16px;align-items:center"><div class="ring"><svg width="14" height="14" viewBox="0 0 24 24"><path fill="#fff" d="M6.6 10.8a15 15 0 006.6 6.6l2.2-2.2c.3-.3.7-.4 1-.2 1.1.4 2.3.6 3.6.6.6 0 1 .4 1 1V20c0 .6-.4 1-1 1A17 17 0 013 4c0-.6.4-1 1-1h3.5c.6 0 1 .4 1 1 0 1.3.2 2.5.6 3.6.1.3 0 .7-.2 1z"/></svg></div><p>+1 555 010 2200</p></div>
  <div style="display:flex;gap:16px;margin-top:20px;align-items:center"><div class="ring"><svg width="15" height="11" viewBox="0 0 16 12"><rect x="1" y="1" width="14" height="10" rx="1" fill="none" stroke="#fff" stroke-width="1.4"/><path d="M1 1l7 6 7-6" stroke="#fff" stroke-width="1.4" fill="none"/></svg></div><p>care@larkhaven.example</p></div>
</div>
<div class="abs fcol" style="left:707px;top:3160px;width:140px">
  <h5>Quick links</h5><div class="u"></div>
  <ul class="links" style="margin-top:12px"><li>Home</li><li>About Us</li><li>Our Services</li><li>Reviews</li><li>Contact Us</li></ul>
</div>
<div class="abs fcol" style="left:868px;top:3160px;width:220px">
  <h5>Subscription</h5><div class="u"></div>
  <div class="subscribe" style="margin-top:30px"><span>Email Address</span><b><svg width="16" height="16" viewBox="0 0 16 16"><path d="M15 1L1 7l6 2 2 6z" fill="#fff"/></svg></b></div>
</div>
<div class="abs fline"></div>
<div class="abs copy">© 2022 Larkhaven Home Care. All Rights Reserved</div>

</body>
</html>
```